Progressive/contemporary business card design for successful Startups as a Service Company

New logo launched in 2020. New website launched in 2021. Now that COVID is (mostly) behind us, I'm networking with more people and need a business card that matches the company/logo design aesthetic.

```html
<!DOCTYPE html>
<html lang="en">
<head>
<meta charset="utf-8">
<title>Quantora Business Card</title>
<link rel="stylesheet" href="https://fonts.googleapis.com/css2?family=Montserrat:wght@400;500;600&display=swap">
<style>
  :root {
    --backdrop: #1e1e1f;
    --card-light: #ffffff;
    --card-dark: #1b1b1c;
    --ink: #3a4558;
    --ink-soft: #4a5466;
    --facet-light: #efefef;
    --facet-dark: #29282a;
    --brand-light: #ffffff;
  }
  * { box-sizing: border-box; margin: 0; padding: 0; }
  html, body {
    width: 1200px;
    height: 1041px;
    overflow: hidden;
    background: var(--backdrop);
    font-family: "Montserrat", sans-serif;
  }
  .canvas {
    position: relative;
    width: 1200px;
    height: 1041px;
  }
  .card {
    position: absolute;
    left: 263px;
    width: 670px;
    height: 384px;
    overflow: hidden;
  }
  .card--front { top: 109px; background: var(--card-light); }
  .card--back { top: 547px; background: var(--card-dark); }

  .front-facets {
    position: absolute;
    left: 277px;
    top: 170px;
    width: 393px;
    height: 214px;
    background: linear-gradient(180deg, #f3f3f3 0%, var(--facet-light) 100%);
    clip-path: polygon(55% 0%, 100% 82.7%, 100% 100%, 0% 100%);
  }
  .holder-name {
    position: absolute;
    left: 33px;
    top: 66px;
    font-weight: 600;
    font-size: 32px;
    letter-spacing: 4.6px;
    color: var(--ink);
    line-height: 1;
  }
  .holder-role {
    position: absolute;
    left: 35px;
    top: 112px;
    font-weight: 600;
    font-size: 19px;
    letter-spacing: 3.2px;
    color: var(--ink);
    line-height: 1;
  }
  .front-brand {
    position: absolute;
    right: 54px;
    top: 82px;
    font-weight: 600;
    font-size: 17px;
    letter-spacing: 2.5px;
    color: var(--ink);
    line-height: 1;
  }
  .contact-list {
    position: absolute;
    left: 34px;
    top: 198px;
    list-style: none;
    color: var(--ink-soft);
    font-size: 15.5px;
    font-weight: 400;
    letter-spacing: 0.2px;
  }
  .contact-item {
    display: flex;
    align-items: flex-start;
    line-height: 24px;
  }
  .contact-item + .contact-item { margin-top: 5px; }
  .contact-item--address { margin-bottom: 10px; }
  .contact-icon {
    width: 16px;
    height: 16px;
    margin-top: 4px;
    margin-right: 16px;
    flex: none;
    fill: var(--ink);
  }
  .back-brand {
    position: absolute;
    left: 0;
    right: 0;
    top: 64px;
    text-align: center;
    font-weight: 500;
    font-size: 46px;
    letter-spacing: 11px;
    color: var(--brand-light);
    line-height: 1;
  }
  .back-facets {
    position: absolute;
    left: 112px;
    top: 177px;
    width: 444px;
    height: 207px;
    background: var(--facet-dark);
    clip-path: polygon(0% 0%, 100% 0%, 74.5% 56%, 54.3% 100%, 45% 100%, 25.9% 56%);
  }
</style>
</head>
<body>
<main class="canvas">
  <section class="card card--front">
    <div class="front-facets" role="img" aria-label="Faint geometric facet decoration"></div>
    <h1 class="holder-name">NAME SURNA</h1>
    <p class="holder-role">YOURPOS</p>
    <p class="front-brand">QUANTORA</p>
    <ul class="contact-list">
      <li class="contact-item contact-item--address">
        <svg class="contact-icon" viewBox="0 0 16 16" aria-hidden="true"><path d="M8 0.5a5.5 5.5 0 0 0-5.5 5.5c0 4 5.5 9.5 5.5 9.5s5.5-5.5 5.5-9.5A5.5 5.5 0 0 0 8 0.5zm0 7.7a2.2 2.2 0 1 1 0-4.4 2.2 2.2 0 0 1 0 4.4z"/></svg>
        <span>418 N Halden Ave., Suite B<br>Marbrook, IL 60999</span>
      </li>
      <li class="contact-item">
        <svg class="contact-icon" viewBox="0 0 16 16" aria-hidden="true"><path d="M4.2 0.8l2 3.4-1.4 1.3c.7 2 1.7 3.6 3.3 5.1l1.5-1 2.6 3-1.6 2.4C6.2 14 2.4 8 3 1.8z"/></svg>
        <span>+56 5550172</span>
      </li>
      <li class="contact-item">
        <svg class="contact-icon" viewBox="0 0 16 16" aria-hidden="true"><path d="M1 6l7-4.5L15 6v8H1zm2 .8v5.7h10V6.8L8 10z"/></svg>
        <span>contact@companyemail.com</span>
      </li>
      <li class="contact-item">
        <svg class="contact-icon" viewBox="0 0 16 16" aria-hidden="true"><path d="M8 1a7 7 0 1 0 0 14A7 7 0 0 0 8 1zm-.6 1.4v2.8H5.2c.5-1.5 1.3-2.5 2.2-2.8zm1.2 0c.9.3 1.7 1.3 2.2 2.8H8.6zM4.9 6.4h2.5v2.6H4.8a9 9 0 0 1 .1-2.6zm3.7 0h2.5a9 9 0 0 1 .1 2.6H8.6zm-6.3 0h1.4a11 11 0 0 0 0 2.6H2.3a5.8 5.8 0 0 1 0-2.6zm10 0h1.4a5.8 5.8 0 0 1 0 2.6h-1.4a11 11 0 0 0 0-2.6zM5.2 10.2h2.2v2.8c-.9-.3-1.7-1.3-2.2-2.8zm3.4 0h2.2c-.5 1.5-1.3 2.5-2.2 2.8z"/></svg>
        <span>companyweb.com</span>
      </li>
    </ul>
  </section>

  <section class="card card--back">
    <p class="back-brand">QUANTORA</p>
    <div class="back-facets" role="img" aria-label="Dark geometric facet decoration"></div>
  </section>
</main>
</body>
</html>
```